Building company with a modern and unique product looking for a business card to help us stand out

We currently have a logo but as our business has grown, we feel that our business card is not reflecting our modern and high quality product and help us stand out from the crowd. Our business is mainly in the construction of new homes using a unique method and materials that makes our homes fire proof, vermin and pest resistant and rated to the maximum cyclone category (category 5). We need a business card that helps us stand out as well as communicating professionalism, high quality and trustworthiness. I have attached our current logo with a black and white option, as well as our business card which is double sided. We would like to retain as much of the information that is currently on our business cards, but presented in a more sleek way. We do like our current colour palette ( white, black, yellow and grey) and have been looking primarily at business cards with a black background however we are open to other combinations of colour and layout as long as we stand out. Please feel free to tweak our logo to make it more suitable for a business card, we like the black option that we use but we have had trouble trying to get the white area to match the rest of the logo and blend effectively into a business card. Please do not hesitate to contact us with any questions as we really want this to be successful!

Target Market(s)

Large contracts including government and larger companies

Industry/Entity Type

Business

We will be providing this business card to potential clients including key government ministers and large funding companies, our business card should show that we are professional and reliable.

Requirements
Must have
• It must be easy to read and pleasing to the eye, It must contain as much of the information on the current business card and unless something really stands out, we will most likely pick a design that has all of the information included. It must include our logo of course and have some colour included.
Nice to have
• We are looking for a high end business card and would like to see designs that reflect this. We like the gloss/matte contrast, plastic cards with opaque/coloured areas and unique features not seen on everyday paper business cards. It would be nice to see a few different colour combinations, we are open to new ideas so please feel free to take some artistic licence.
Should not have
• Must not be too busy, difficult to read or be distracting from the information conveyed. Other than this please feel free to add your own touches and make it unique!

```html
<!DOCTYPE html>
<html lang="en">
<head>
<meta charset="utf-8">
<title>Ridgeline Building Company – Business Card</title>
<link rel="stylesheet" href="https://fonts.googleapis.com/css2?family=Open+Sans:wght@400;600&family=Tinos:wght@400&display=swap">
<style>
  :root {
    --ink: #0b0b0b;
    --paper: #ffffff;
    --paper-shade: #f1f1f1;
    --gold: #cdb935;
    --grey: #8a8a8a;
    --backdrop: #e6e3de;
  }
  html, body {
    margin: 0;
    width: 1200px;
    height: 780px;
    overflow: hidden;
    background: var(--backdrop);
  }
  .canvas {
    position: relative;
    width: 1200px;
    height: 780px;
  }
  .card {
    position: absolute;
    width: 580px;
    height: 331px;
    background: linear-gradient(160deg, var(--paper) 0%, var(--paper-shade) 100%);
    box-shadow: 0 10px 24px rgba(0,0,0,0.22);
    overflow: hidden;
  }
  .card--front { left: 50px; top: 60px; }
  .card--back { left: 590px; top: 400px; }

  /* Brand wordmark */
  .brand {
    display: flex;
    align-items: center;
    gap: 14px;
    font-family: "Open Sans", sans-serif;
    font-weight: 600;
    color: var(--ink);
  }
  .brand__mark {
    width: 18px;
    height: 18px;
    background: var(--gold);
  }
  .brand__name {
    display: flex;
    flex-direction: column;
    line-height: 1.05;
  }
  .brand__primary { font-size: 40px; letter-spacing: 2px; }
  .brand__secondary { font-size: 17px; letter-spacing: 1px; align-self: flex-end; }

  /* Front */
  .front__logo-area {
    position: absolute;
    left: 0; top: 0;
    width: 100%;
    height: 190px;
    display: flex;
    align-items: center;
    justify-content: center;
  }
  .front__title-band {
    position: absolute;
    left: 0; top: 190px;
    width: 100%;
    height: 36px;
    background: var(--gold);
    display: flex;
    align-items: center;
    padding-left: 64px;
    box-sizing: border-box;
    font-family: "Open Sans", sans-serif;
    font-size: 19px;
    color: var(--paper);
  }
  .front__title-band .role { font-size: 16px; }
  .front__contact {
    position: absolute;
    left: 0; top: 226px;
    width: 100%;
    height: 105px;
    background: var(--ink);
    padding: 16px 0 0 150px;
    box-sizing: border-box;
    font-family: "Tinos", serif;
    font-size: 15px;
    line-height: 1.45;
    color: var(--paper);
  }
  .contact__label { color: var(--gold); }

  /* Back */
  .back__logo-area {
    position: absolute;
    left: 0; top: 40px;
    width: 100%;
    display: flex;
    justify-content: center;
  }
  .back__tagline {
    position: absolute;
    left: 0; top: 200px;
    width: 100%;
    text-align: center;
    font-family: "Tinos", serif;
    font-size: 17px;
    color: var(--gold);
  }
  .back__band {
    position: absolute;
    left: 0; bottom: 34px;
    width: 100%;
    height: 38px;
    background: var(--ink);
    display: flex;
    align-items: center;
    justify-content: center;
    font-family: "Tinos", serif;
    font-size: 17px;
    color: var(--paper);
    letter-spacing: 0.3px;
  }
</style>
</head>
<body>
<main class="canvas">

  <section class="card card--front" aria-label="Business card front">
    <div class="front__logo-area">
      <div class="brand">
        <span class="brand__mark"></span>
        <span class="brand__name">
          <span class="brand__primary">RIDGELINE</span>
          <span class="brand__secondary">Building Company</span>
        </span>
      </div>
    </div>
    <div class="front__title-band">
      Marcus Keller&nbsp;|&nbsp;<span class="role">Managing Director</span>
    </div>
    <div class="front__contact">
      <div><span class="contact__label">cell:</span> 0400 555 217</div>
      <div><span class="contact__label">office:</span> (02) 5550 3184</div>
      <div><span class="contact__label">email:</span> office@ridgelinebuild.com</div>
    </div>
  </section>

  <section class="card card--back" aria-label="Business card back">
    <div class="back__logo-area">
      <div class="brand">
        <span class="brand__mark"></span>
        <span class="brand__name">
          <span class="brand__primary">RIDGELINE</span>
          <span class="brand__secondary">Building Company</span>
        </span>
      </div>
    </div>
    <p class="back__tagline">Specialising in Homes that are</p>
    <div class="back__band">Fire Proof | Climate Proof | Cyclone Rated(cat.5)</div>
  </section>

</main>
</body>
</html>
```